コンセプトや情報は添付ファイルに書いてますので、それを基に作成お願いします

【注意事項】

※尚、キャバクラやバーにもpopを置くので高級かつ洗練されたデザインを意識してください。

※カラーやフォントの指定はありませんが、いわゆるポスター作成ソフト等によくあるテンプレートを使ったデザインはあまり好ましくありません

※急ぎですので、レスポンスよく返せる方を希望します。

※写真等は何もないのですが、月末には写真素材が届きます。写真素材を使うデザインの場合取り急ぎ、別の素材で代用してください
ロゴのaiデータです

秀逸です

ありがとうございます

```html
<!DOCTYPE html>
<html lang="ja">
<head>
<meta charset="utf-8">
<title>KAGARI Grand Open</title>
<link rel="stylesheet" href="https://fonts.googleapis.com/css2?family=Cormorant+Garamond:wght@400;500;600&family=Noto+Serif+JP:wght@400;500;600&display=swap">
<style>
  :root {
    --charcoal: #2a2928;
    --khaki: #d2cc8c;
    --ivory: #f2efe6;
    --ink: #2b2a27;
    --serif-latin: "Cormorant Garamond", "Noto Serif JP", serif;
    --serif-jp: "Noto Serif JP", serif;
  }
  * { margin: 0; padding: 0; box-sizing: border-box; }
  html, body { width: 854px; height: 1200px; overflow: hidden; background: var(--charcoal); }
  .poster { position: relative; width: 854px; height: 1200px; background: var(--charcoal); color: var(--ivory); font-family: var(--serif-latin); }

  .date-block { position: absolute; left: 0; top: 150px; width: 854px; height: 120px; }
  .date { position: absolute; left: 205px; top: 0; font-size: 118px; font-weight: 500; line-height: 1; letter-spacing: -2px; }
  .weekday { position: absolute; left: 322px; top: 14px; font-size: 26px; font-weight: 600; writing-mode: vertical-rl; letter-spacing: 2px; }
  .date-divider { position: absolute; left: 362px; top: 12px; width: 2px; height: 92px; background: var(--ivory); }
  .time { position: absolute; left: 382px; top: 14px; font-size: 44px; font-weight: 500; line-height: 1.02; }

  .date-rule { position: absolute; left: 205px; top: 280px; width: 445px; height: 2px; background: var(--ivory); }
  .grand-open { position: absolute; left: 0; top: 294px; width: 854px; text-align: center; font-size: 50px; font-weight: 500; letter-spacing: 1px; }

  .brand { position: absolute; left: 0; top: 520px; width: 854px; text-align: center; }
  .brand-dot { display: block; width: 14px; height: 14px; border-radius: 50%; background: var(--ivory); margin: 0 auto 22px; }
  .brand-name { font-size: 34px; font-weight: 500; letter-spacing: 8px; padding-left: 8px; }

  .lower { position: absolute; left: 0; top: 818px; width: 854px; height: 382px; background: var(--khaki); color: var(--ink); }
  .tagline { position: absolute; left: 0; top: 52px; width: 854px; text-align: center; font-family: var(--serif-jp); font-size: 60px; font-weight: 500; letter-spacing: 14px; line-height: 1; }
  .tagline-rule { position: absolute; left: 94px; top: 146px; width: 666px; height: 1px; background: var(--ink); }

  .info-label { position: absolute; left: 108px; top: 170px; font-size: 13px; letter-spacing: 2px; }
  .info-box { position: absolute; left: 86px; top: 192px; width: 336px; height: 138px; border: 1px solid var(--ink); padding: 18px 20px; font-size: 13px; line-height: 1.7; letter-spacing: 1px; }
  .info-box .hours { margin-bottom: 22px; }
  .info-box .hours span { display: block; padding-left: 120px; }

  .contact { position: absolute; left: 500px; top: 200px; }
  .tel { font-size: 24px; letter-spacing: 2px; margin-bottom: 14px; }
  .shop { font-family: var(--serif-jp); font-size: 21px; letter-spacing: 1px; margin-bottom: 8px; }
  .address { font-family: var(--serif-jp); font-size: 13px; line-height: 1.6; letter-spacing: 1px; }
</style>
</head>
<body>
<main class="poster">
  <section class="date-block">
    <div class="date">7/4</div>
    <div class="weekday">SAT</div>
    <div class="date-divider"></div>
    <div class="time">PM<br>18:00 -</div>
  </section>
  <div class="date-rule"></div>
  <h1 class="grand-open">GRAND OPEN</h1>

  <div class="brand">
    <span class="brand-dot"></span>
    <div class="brand-name">KAGARI</div>
  </div>

  <section class="lower">
    <p class="tagline">新感覚の焼肉 bar</p>
    <div class="tagline-rule"></div>

    <div class="info-label">INFORMATION</div>
    <div class="info-box">
      <p class="hours">OPEN&nbsp;&nbsp;18:00~5:00<span>/&nbsp;&nbsp;CLOSE&nbsp;&nbsp;SUNDAY</span></p>
      <p>FAX&nbsp;&nbsp;052-000-5678<br>LINE&nbsp;&nbsp;@XXXXXXXXX</p>
    </div>

    <div class="contact">
      <p class="tel">TEL&nbsp;&nbsp;052-000-1234</p>
      <p class="shop">高級焼肉 bar&nbsp;&nbsp;KA GA RI</p>
      <p class="address">愛知県名古屋市中区錦2-8-15<br>榊ビル2F</p>
    </div>
  </section>
</main>
</body>
</html>
```